Plumber Referal Program for Water Damage Mitigation

A flyer describing incentives for plumbers to refer us as well as business information. We are called Volmar Restoration and we offer water damage mitigation, mold remediation, and sewage clean up as our 3 services. We are using blue as our company color, here are the following codes included in the logo.

Lighter blue, middle section of logo:
HEX: #2499c7
rgb(36,153,199)
hsl(197,69%,46%)

Darker blue, main color of logo and lettering:
HEX: #1a7da4
rgb(26,125,164)
hsl(197,73%,37%)

Lightest blue, only on small stars at top of logo:
HEX: #9bd3fc
rgb(155,211,252)
hsl(205,94%,80%)

Target Market(s)

Plumbers and other service industries.

Industry/Entity Type

Water Damage Restoration

Requirements
Must have
• Name of our company (Volmar Restoration) along with our number 1(800)614-2297. Website is volmarrestoration.example. 24/7 emergency response. Different methods of payment, including Paylink, Trovo, Coin Pouch, and written checks. Please include 60-90 minute response time. Please include our 3 services, water damage mitigation, mold remediation, and sewage clean-up. A simple 2 sided flyer.
Nice to have
• Fairly simple design, not too busy. At least 1-2 pictures of water damage and/or mold remediation.
Should not have
• A dollar amount, we would like it to be open ended. Stock photos of smiling people.

```html
<!DOCTYPE html>
<html lang="en">
<head>
<meta charset="utf-8">
<title>Volmar Restoration – Plumber Referral Flyer</title>
<link rel="stylesheet" href="https://fonts.googleapis.com/css2?family=Montserrat:ital,wght@0,500;0,600;1,800&family=Dosis:wght@600;700&family=Nunito:wght@500&family=Arimo&display=swap">
<style>
  :root {
    --blue-dark: #1a7da4;
    --blue-mid: #2499c7;
    --blue-light: #9bd3fc;
    --white: #ffffff;
    --text: #2c2c2c;
    --page-bg: #c6c6c6;
  }
  * { margin: 0; padding: 0; box-sizing: border-box; }
  html, body { width: 1200px; height: 787px; overflow: hidden; background: var(--page-bg); }
  .canvas { position: relative; width: 1200px; height: 787px; }

  .flyer {
    position: absolute; width: 457px; height: 645px; overflow: hidden;
    background: var(--white);
  }
  .side-front { left: 90px; top: 82px; }
  .side-back { left: 637px; top: 77px; }
  .flyer-shapes { position: absolute; left: 0; top: 0; }

  .headline {
    position: absolute; left: 14px; top: 22px;
    font-family: "Montserrat", sans-serif; font-style: italic; font-weight: 800;
    color: var(--blue-dark); font-size: 14px; line-height: 14px; letter-spacing: 1.9px;
  }
  .headline span { display: block; font-size: 12.5px; line-height: 13px; letter-spacing: 1.75px; }

  .brand-mark {
    position: absolute; left: 354px; top: 168px; width: 46px; height: 46px;
    border-radius: 50%; background: var(--blue-dark);
  }
  .brand-name {
    position: absolute; left: 306px; top: 221px; width: 144px; text-align: center;
    font-family: "Dosis", sans-serif; font-weight: 700; font-size: 15px; line-height: 18px;
    color: var(--blue-dark);
  }

  .section-title {
    position: absolute; font-family: "Dosis", sans-serif; font-weight: 600;
    color: var(--blue-dark); font-size: 20px; line-height: 22px; text-transform: uppercase;
  }
  .response-title { left: 36px; top: 316px; }
  .services-title { left: 235px; top: 318px; }

  .about-box {
    position: absolute; left: 31px; top: 364px; width: 132px; height: 115px;
    background: var(--blue-mid); border-radius: 5px; color: var(--white);
    font-family: "Nunito", sans-serif; font-size: 9.6px; line-height: 13.6px;
    padding: 9px 8px 0 12px;
  }

  .service-list {
    position: absolute; left: 237px; top: 344px; list-style: none;
    font-family: "Nunito", sans-serif; font-size: 13.5px; color: var(--text);
  }
  .service-list li { display: flex; align-items: center; height: 24.7px; }
  .service-list svg { width: 10px; height: 10px; margin-right: 8px; }

  .contact-card {
    position: absolute; left: 230px; top: 441px; width: 185px; height: 166px;
    border-radius: 4px; overflow: hidden; background: var(--blue-mid);
    box-shadow: 0 5px 7px rgba(0,0,0,0.18); text-align: center; color: var(--white);
  }
  .contact-head { background: var(--blue-dark); height: 66px; padding-top: 12px; }
  .contact-name { font-family: "Dosis", sans-serif; font-weight: 700; font-size: 15px; line-height: 18px; }
  .contact-phone { font-family: "Montserrat", sans-serif; font-weight: 600; font-size: 19px; line-height: 26px; }
  .contact-rows { list-style: none; font-family: "Arimo", sans-serif; font-size: 8.6px; padding: 0 6px; }
  .contact-rows li { height: 23px; line-height: 23px; white-space: nowrap; }
  .contact-rows li.ruled { border-bottom: 1px solid rgba(255,255,255,0.75); margin: 0 8px; }

  .website {
    position: absolute; left: 200px; top: 616px; width: 250px; text-align: center;
    font-family: "Montserrat", sans-serif; font-weight: 500; font-size: 12px; line-height: 16px;
    color: var(--white); letter-spacing: 1px; white-space: nowrap;
  }
</style>
</head>
<body>
<div class="canvas">

  <!-- Front side -->
  <div class="flyer side-front">
    <svg class="flyer-shapes" width="457" height="645" viewBox="0 0 457 645">
      <defs>
        <linearGradient id="frontPhotoTone" x1="0" y1="0" x2="1" y2="1">
          <stop offset="0" stop-color="#e2dfdc"/>
          <stop offset="0.6" stop-color="#b9b4b0"/>
          <stop offset="1" stop-color="#8d8784"/>
        </linearGradient>
        <linearGradient id="frontFamilyTone" x1="0" y1="0" x2="1" y2="1">
          <stop offset="0" stop-color="#c1a371"/>
          <stop offset="1" stop-color="#5d5a63"/>
        </linearGradient>
      </defs>
      <path role="img" aria-label="Photo of a plumber tightening a white sink trap pipe with a red wrench"
            d="M0 0H457V270C380 295 240 300 0 232Z" fill="url(#frontPhotoTone)"/>
      <path d="M0 232C120 285 250 296 345 268L352 286C250 318 120 300 0 258Z" fill="var(--blue-dark)"/>
      <path d="M0 250C125 300 255 306 348 280" fill="none" stroke="var(--blue-light)" stroke-width="4"/>
      <path d="M85 288C180 305 290 306 360 282" fill="none" stroke="var(--blue-mid)" stroke-width="6"/>
      <circle cx="378" cy="216" r="83" fill="var(--white)" stroke="var(--blue-dark)" stroke-width="5"/>
      <path d="M457 552C400 556 360 566 320 580" fill="none" stroke="var(--blue-light)" stroke-width="8"/>
      <path d="M0 540C45 595 110 618 180 618C280 615 360 588 457 572V645H0Z" fill="var(--blue-dark)"/>
      <path d="M0 575C30 600 60 612 95 612" fill="none" stroke="var(--white)" stroke-width="2"/>
      <circle cx="134" cy="568" r="82" fill="var(--blue-light)"/>
      <circle role="img" aria-label="Photo of a family in a home catching water leaking from the ceiling"
              cx="126" cy="570" r="80" fill="url(#frontFamilyTone)" stroke="var(--white)" stroke-width="2.5"/>
    </svg>

    <h1 class="headline">Plumber Referal Program<span>for Water Damage Mitigation</span></h1>
    <div class="brand-mark"></div>
    <div class="brand-name">VOLMAR RESTORATION</div>

    <h2 class="section-title response-title">60-90 Minute<br>Response Time</h2>
    <p class="about-box">We are called Volmar Restoration and we offer water damage mitigation, mold remediation, and sewage clean up as our 3 services</p>

    <h2 class="section-title services-title">Services</h2>
    <ul class="service-list">
      <li><svg viewBox="0 0 12 12"><path d="M1 6.5L4.5 10L11 2" fill="none" stroke="var(--blue-mid)" stroke-width="2"/></svg>Water damage mitigation</li>
      <li><svg viewBox="0 0 12 12"><path d="M1 6.5L4.5 10L11 2" fill="none" stroke="var(--blue-mid)" stroke-width="2"/></svg>Mold remediation and</li>
      <li><svg viewBox="0 0 12 12"><path d="M1 6.5L4.5 10L11 2" fill="none" stroke="var(--blue-mid)" stroke-width="2"/></svg>Sewage clean-up</li>
    </ul>

    <div class="contact-card">
      <div class="contact-head">
        <div class="contact-name">VOLMAR RESTORATION</div>
        <div class="contact-phone">1(800)614-2297</div>
      </div>
      <ul class="contact-rows">
        <li class="ruled">24/7 emergency response</li>
        <li class="ruled">Different methods of payment</li>
        <li>including Paylink, Trovo, Coin Pouch</li>
        <li>and written checks</li>
      </ul>
    </div>

    <div class="website">www.volmarrestoration.example</div>
  </div>

  <!-- Back side -->
  <div class="flyer side-back">
    <svg class="flyer-shapes" width="457" height="645" viewBox="0 0 457 645">
      <defs>
        <linearGradient id="backPhotoTone" x1="0" y1="0" x2="1" y2="1">
          <stop offset="0" stop-color="#e6e2dc"/>
          <stop offset="0.55" stop-color="#b8aea4"/>
          <stop offset="1" stop-color="#6f6a68"/>
        </linearGradient>
        <linearGradient id="backFamilyTone" x1="0" y1="0" x2="1" y2="1">
          <stop offset="0" stop-color="#c1a371"/>
          <stop offset="1" stop-color="#5d5a63"/>
        </linearGradient>
      </defs>
      <path role="img" aria-label="Photo of a gloved hand turning a wrench on brass pipe fittings"
            d="M0 0H457V270C380 295 240 300 0 232Z" fill="url(#backPhotoTone)"/>
      <path d="M0 232C120 285 250 296 345 268L352 286C250 318 120 300 0 258Z" fill="var(--blue-dark)"/>
      <path d="M0 250C125 300 255 306 348 280" fill="none" stroke="var(--blue-light)" stroke-width="4"/>
      <path d="M85 288C180 305 290 306 360 282" fill="none" stroke="var(--blue-mid)" stroke-width="6"/>
      <circle cx="378" cy="216" r="83" fill="var(--white)" stroke="var(--blue-dark)" stroke-width="5"/>
      <path d="M457 552C400 556 360 566 320 580" fill="none" stroke="var(--blue-light)" stroke-width="8"/>
      <path d="M0 540C45 595 110 618 180 618C280 615 360 588 457 572V645H0Z" fill="var(--blue-dark)"/>
      <path d="M0 575C30 600 60 612 95 612" fill="none" stroke="var(--white)" stroke-width="2"/>
      <circle cx="134" cy="568" r="82" fill="var(--blue-light)"/>
      <circle role="img" aria-label="Photo of a family in a home catching water leaking from the ceiling"
              cx="126" cy="570" r="80" fill="url(#backFamilyTone)" stroke="var(--white)" stroke-width="2.5"/>
    </svg>

    <h1 class="headline">Plumber Referal Program<span>for Water Damage Mitigation</span></h1>
    <div class="brand-mark"></div>
    <div class="brand-name">VOLMAR RESTORATION</div>

    <h2 class="section-title response-title">60-90 Minute<br>Response Time</h2>
    <p class="about-box">We are called Volmar Restoration and we offer water damage mitigation, mold remediation, and sewage clean up as our 3 services</p>

    <h2 class="section-title services-title">Services</h2>
    <ul class="service-list">
      <li><svg viewBox="0 0 12 12"><path d="M1 6.5L4.5 10L11 2" fill="none" stroke="var(--blue-mid)" stroke-width="2"/></svg>Water damage mitigation</li>
      <li><svg viewBox="0 0 12 12"><path d="M1 6.5L4.5 10L11 2" fill="none" stroke="var(--blue-mid)" stroke-width="2"/></svg>Mold remediation and</li>
      <li><svg viewBox="0 0 12 12"><path d="M1 6.5L4.5 10L11 2" fill="none" stroke="var(--blue-mid)" stroke-width="2"/></svg>Sewage clean-up</li>
    </ul>

    <div class="contact-card">
      <div class="contact-head">
        <div class="contact-name">VOLMAR RESTORATION</div>
        <div class="contact-phone">1(800)614-2297</div>
      </div>
      <ul class="contact-rows">
        <li class="ruled">24/7 emergency response</li>
        <li class="ruled">Different methods of payment</li>
        <li>including Paylink, Trovo, Coin Pouch</li>
        <li>and written checks</li>
      </ul>
    </div>

    <div class="website">www.volmarrestoration.example</div>
  </div>

</div>
</body>
</html>
```